Corvath Holdings, LLC

We are a design build general contracting company.
We work with commercial accounts and private developers. We build retail spaces, restaurants and housing projects.
Im looking for a clean professional type of logo incorporating a roman flavor, think ionic columns and pedestals.
Two toned colorway.
I like unusual fonts and Im not afraid to do something bold with the logo.
Contact Information for Business Card
Marisol Brenkowitz
318-472-9051 corvathmb@mailvexo.com
Font styles to use
Decorative
Colors
Designer to choose colors to be used in the design.
Requirements
Should not have
- I don't like reds pinks.

```html
<!DOCTYPE html>
<html lang="en">
<head>
<meta charset="utf-8">
<title>Corvath Construction and Development — Business Card</title>
<link href="https://fonts.googleapis.com/css2?family=Cinzel:wght@400;600&family=Open+Sans:wght@400&display=swap" rel="stylesheet">
<style>
  :root {
    --backdrop: #2b2b2d;
    --card-dark: #0c0c0d;
    --card-light: #1c1c1e;
    --brand-blue: #1c76ac;
    --brand-blue-light: #2a8fcb;
    --text-light: #d4d6d8;
    --divider: #6c6e70;
  }
  * { margin: 0; padding: 0; box-sizing: border-box; }
  html, body {
    width: 1200px;
    height: 900px;
    overflow: hidden;
    background: var(--backdrop);
  }
  .canvas {
    position: relative;
    width: 1200px;
    height: 900px;
  }
  .card {
    position: absolute;
    width: 560px;
    height: 320px;
    background: linear-gradient(135deg, var(--card-light) 0%, var(--card-dark) 70%);
    box-shadow: 0 14px 30px rgba(0,0,0,0.45);
    overflow: hidden;
  }
  .card__band {
    position: absolute;
    left: 0; right: 0; bottom: 0;
    height: 12px;
    background: linear-gradient(90deg, var(--brand-blue), var(--brand-blue-light), var(--brand-blue));
  }
  .card--front { left: 380px; top: 90px; }
  .card--back  { left: 200px; top: 470px; }

  .brand {
    position: absolute;
    inset: 0 0 12px 0;
    display: flex;
    align-items: center;
    justify-content: center;
  }
  .brand__name {
    font-family: "Cinzel", serif;
    font-weight: 600;
    color: var(--brand-blue);
    font-size: 30px;
    letter-spacing: 2px;
    text-align: center;
    line-height: 1.25;
  }

  .contact-layout {
    position: absolute;
    inset: 0 0 12px 0;
    display: flex;
    align-items: center;
    padding-left: 48px;
  }
  .holder-name {
    font-family: "Cinzel", serif;
    font-weight: 600;
    color: var(--brand-blue);
    font-size: 19px;
    letter-spacing: 1.5px;
    width: 240px;
    margin-bottom: 26px;
  }
  .divider {
    width: 1px;
    height: 80px;
    background: var(--divider);
    margin: 0 22px 0 8px;
  }
  .contact-list { list-style: none; }
  .contact-list li {
    display: flex;
    align-items: center;
    font-family: "Open Sans", sans-serif;
    font-size: 16px;
    color: var(--text-light);
    margin: 4px 0;
  }
  .contact-icon {
    width: 20px;
    height: 20px;
    margin-right: 8px;
    flex: none;
  }
</style>
</head>
<body>
<main class="canvas">
  <section class="card card--front" aria-label="Card front">
    <div class="brand">
      <p class="brand__name">CORVATH<br>CONSTRUCTION AND DEVELOPMENT</p>
    </div>
    <div class="card__band"></div>
  </section>

  <section class="card card--back" aria-label="Card back">
    <div class="contact-layout">
      <p class="holder-name">MARISOL BRENKOWITZ</p>
      <div class="divider"></div>
      <ul class="contact-list">
        <li>
          <svg class="contact-icon" viewBox="0 0 20 20" aria-hidden="true">
            <circle cx="10" cy="10" r="10" fill="#1c76ac"/>
            <path d="M6.5 5.5c.6-.5 1.4-.4 1.8.2l.9 1.4c.3.5.2 1.1-.2 1.4l-.6.5c.5 1.1 1.3 2 2.4 2.6l.5-.6c.4-.4 1-.5 1.4-.2l1.4.9c.6.4.7 1.2.2 1.8l-.6.7c-.6.6-1.6.8-2.4.4-2.2-1.1-4-2.9-5.1-5.1-.4-.8-.2-1.8.4-2.4z" fill="#0d0d0d"/>
          </svg>
          318-472-9051
        </li>
        <li>
          <svg class="contact-icon" viewBox="0 0 20 20" aria-hidden="true">
            <circle cx="10" cy="10" r="10" fill="#1c76ac"/>
            <rect x="5" y="6.5" width="10" height="7" rx="1" fill="#0d0d0d"/>
            <path d="M5.5 7l4.5 3.5L14.5 7" fill="none" stroke="#1c76ac" stroke-width="1"/>
          </svg>
          corvathmb@mailvexo.com
        </li>
        <li>
          <svg class="contact-icon" viewBox="0 0 20 20" aria-hidden="true">
            <circle cx="10" cy="10" r="10" fill="#1c76ac"/>
            <circle cx="10" cy="10" r="5" fill="none" stroke="#0d0d0d" stroke-width="1.3"/>
            <ellipse cx="10" cy="10" rx="2.2" ry="5" fill="none" stroke="#0d0d0d" stroke-width="1.1"/>
            <line x1="5" y1="10" x2="15" y2="10" stroke="#0d0d0d" stroke-width="1.1"/>
          </svg>
          www.corvathbuild.com
        </li>
      </ul>
    </div>
    <div class="card__band"></div>
  </section>
</main>
</body>
</html>
```